Tech and Gadget Blog - News Site

I'm looking for someone to help design a wordpress theme for a tech news site that I'm creating.

I'll need the elements to be from right to left please because it's going to be in Arabic.

There are three main elements to the site.
1) We'll be publishing news on a daily basis (blog style) - Wirecove style

2) We'll have a section dedicated to the different programs we produce on clipvane (so people should be able to view our latest content but also be able to filter based on the program.

3) We want it to be easy for people to comment and share (so having a good sharebar (like spreadnest) and using remarko will be important too.

Of course it's important for us to have positions for banners so that we can monetize the site too and that the site is responsive.

You can see our channel here https://www.clipvane.com/channel/UC8mkrwpqLEZHBNa3t-x_Rb

One other very important page is a page for people to submit interest for advertising and advertorials. So that page will need to look very professional.

Target Market(s)

tech focused

Industry/Entity Type

Media

Coding

Coded - Design and coding required

Number of Pages Required

5+ page

Font styles to use
Sans Serif

Colors
09ab93
f59195
ffffff

Requirements
Must have
• using Wordpress as the CMS

```html
<!DOCTYPE html>
<html lang="en">
<head>
<meta charset="utf-8">
<title>Nabdi TV – Tech News</title>
<link rel="stylesheet" href="https://fonts.googleapis.com/css2?family=Roboto:wght@400;700&family=Roboto+Condensed:wght@400;700&display=swap">
<style>
:root{
  --teal:#09ab93;
  --teal-soft:#5cc3b3;
  --teal-pale:#d8f1ec;
  --coral:#f59195;
  --orange:#f26a3d;
  --white:#ffffff;
  --ink:#333333;
  --muted:#7a7a7a;
  --line:#e2e2e2;
  --fb:#3b5a98;
  --tw:#2fa9e0;
  --pin:#cb2027;
}
*{box-sizing:border-box;margin:0;padding:0}
html,body{width:1200px;height:2786px;overflow:hidden}
body{font-family:"Roboto",Arial,sans-serif;color:var(--ink);font-size:10px;line-height:1.35;
  background:linear-gradient(90deg,#eaf6f4 0,#ffffff 50%,#eaf6f4 100%);position:relative}
.side-ad{position:absolute;width:240px;height:700px;border-radius:4px;
  background:linear-gradient(160deg,#e9f6f3 0%,#bfe6df 45%,#f7d6d7 75%,#e9f6f3 100%)}
.page{position:absolute;left:251px;top:0;width:696px;height:2786px;background:var(--white);
  border-left:3px solid var(--teal-soft);border-right:3px solid var(--teal-soft);box-shadow:0 0 12px rgba(0,0,0,.12)}
.abs{position:absolute}

/* header */
.brand{left:46px;top:22px;display:flex;align-items:center;gap:10px}
.brand-dot{width:62px;height:62px;border-radius:50%;background:var(--teal)}
.brand-name{font-family:"Roboto Condensed",sans-serif;font-weight:700;font-size:26px;color:var(--teal);white-space:nowrap}
.newsletter{right:60px;top:16px;display:flex;align-items:center;gap:8px;font-family:"Roboto Condensed",sans-serif}
.newsletter label{color:var(--teal);font-size:12px;letter-spacing:.5px}
.newsletter .field{width:106px;height:18px;border:1px solid var(--line);font-size:9px;color:#999;padding:3px 5px}
.newsletter .btn{background:var(--orange);color:#fff;font-size:10px;font-weight:700;padding:3px 7px}
.connect{right:60px;top:80px;display:flex;align-items:center;gap:6px;font-family:"Roboto Condensed",sans-serif;font-size:12px;color:var(--teal);white-space:nowrap}
.connect b{color:var(--coral);font-weight:400}
.soc{width:20px;height:20px;border-radius:50%;display:inline-block;flex:none}
.soc.c{background:var(--coral)} .soc.t{background:var(--teal)}
.header-rule{left:20px;right:20px;top:116px;border-top:2px solid var(--teal-pale)}

/* nav */
.nav{left:50px;top:139px;width:594px;height:21px;background:var(--teal);display:flex;align-items:center;
  font-family:"Roboto Condensed",sans-serif;font-size:10px;color:#fff}
.nav a{padding:0 15px;height:21px;line-height:21px;text-decoration:none;color:#fff}
.nav a.home{background:var(--orange)} .nav a.alt{background:var(--coral)} .nav a.dark{background:#444}
.nav .search{margin-left:auto;margin-right:5px;width:120px;height:14px;background:#fff;border-radius:8px;color:#999;font-size:8px;padding:1px 7px}
.hero{left:50px;top:163px;width:594px;height:260px;border:4px solid var(--teal-soft);
  background:linear-gradient(120deg,#3d4a4f 0%,#cfe9e4 40%,#f4f6f6 60%,#8fb9b3 100%)}

/* section heads */
.sec-title{left:50px;top:447px;font-family:"Roboto Condensed",sans-serif;font-weight:700;font-size:18px;color:var(--teal)}
.sec-title span{color:var(--coral)}
.stories{left:50px;top:475px;width:594px;display:flex;gap:8px}
.story{width:192px}
.story .ph{height:106px;background:linear-gradient(135deg,#8b9a8c,#d9e5e2 50%,#e27d7d)}
.story:nth-child(2) .ph{background:linear-gradient(135deg,#1a3d7a,#c9d6ea 50%,#e24b55)}
.story:nth-child(3) .ph{background:linear-gradient(135deg,#09ab93,#c8ece5 55%,#3a3a3a)}
.story .tag{height:18px;background:var(--coral);color:#fff;font-family:"Roboto Condensed",sans-serif;font-weight:700;font-size:10px;line-height:18px;padding-left:10px;position:relative}
.story .tag::before{content:"";position:absolute;left:2px;top:5px;border:4px solid transparent;border-left-color:#fff}
.story p{font-weight:700;font-size:9px;color:var(--teal);margin-top:7px;line-height:1.35}
.arrow-l,.arrow-r{top:587px;width:0;height:0;border:6px solid transparent}
.arrow-l{left:34px;border-right-color:var(--teal)} .arrow-r{left:650px;border-left-color:var(--teal)}

/* posts */
.post{left:46px;width:394px}
.post-head{display:flex;gap:8px}
.date{width:40px;flex:none;text-align:center;font-family:"Roboto Condensed",sans-serif;font-weight:700}
.date .d{background:var(--coral);color:#fff;font-size:17px;height:26px;line-height:26px}
.date .m{background:var(--teal);color:#fff;font-size:9px;height:13px;line-height:13px}
.post-title{font-family:"Roboto Condensed",sans-serif;font-weight:700;font-size:18px;line-height:1.25;color:var(--teal)}
.post-title span{color:var(--coral)}
.excerpt{font-size:8.5px;color:var(--muted);line-height:1.45;margin-top:10px}
.figure{margin-top:10px;border:1px solid var(--line);padding:7px;height:340px}
.figure .main{height:245px;background:linear-gradient(120deg,#f2f2f2,#9fd8cf 35%,#3d3d3d 60%,#e05a63)}
.thumbs{display:flex;gap:6px;margin-top:7px}
.thumbs i{flex:1;height:70px;background:linear-gradient(135deg,#cde9e4,#6b7d86 60%,#f2b6b9)}
.meta{display:flex;justify-content:space-between;margin-top:8px;font-size:8.5px;color:#555}
.meta .cm{color:var(--muted);margin-right:110px}
.meta .cm::before{content:"";display:inline-block;width:9px;height:7px;background:var(--coral);border-radius:2px;margin-right:4px}
.share{display:flex;align-items:center;gap:4px;margin-top:14px}
.sb{height:14px;line-height:14px;color:#fff;font-size:8px;font-weight:700;padding:0 8px;border-radius:2px}
.sb.tw{background:var(--tw)} .sb.fb{background:var(--fb)} .sb.pin{background:#fff;color:var(--pin);border:1px solid var(--line);line-height:12px}
.cnt{height:14px;line-height:12px;border:1px solid var(--line);font-size:7px;color:#777;padding:0 5px;margin-right:12px}
.share .icons{margin-left:auto;display:flex;gap:3px}
.share .icons i{width:16px;height:16px;border-radius:50%;background:#2b6f66;display:block}
.video{margin-top:10px;border:1px solid var(--line);padding:7px;height:405px}
.video .screen{height:240px;position:relative;background:linear-gradient(180deg,#0c1224 0%,#2a2f55 40%,#b0633a 70%,#201d2c 100%)}
.video .bar{position:absolute;left:8px;right:8px;bottom:8px;height:3px;background:rgba(255,255,255,.4)}
.video .bar::before{content:"";position:absolute;left:0;top:0;width:22%;height:3px;background:var(--coral)}
.video .play{position:absolute;left:50%;top:50%;transform:translate(-50%,-50%)}
.vthumbs{display:grid;grid-template-columns:repeat(4,1fr);gap:6px;margin-top:7px}
.vthumbs i{height:68px;background:linear-gradient(135deg,#3b3f4a,#d6d6d6 55%,#d8535c)}
.pub{font-size:8px;color:#555;margin-top:4px}
.pager{margin-left:auto;font-size:9px;color:var(--coral);font-weight:700;white-space:nowrap;padding-top:6px}

/* comments */
.comments{margin-top:8px;font-size:8px;color:#555}
.comments .count{font-weight:700;border-bottom:1px solid var(--line);padding-bottom:5px}
.compose{display:flex;gap:6px;margin-top:8px;align-items:center}
.av{width:22px;height:22px;background:#c9d2d6;flex:none}
.compose .box{flex:1;height:24px;border:1px solid var(--line);padding:6px;color:#aaa}
.sort{display:inline-block;border:1px solid var(--line);padding:2px 6px;margin:14px 0 6px;font-weight:700}
.c-item{display:flex;gap:6px;margin-top:10px}
.c-item .name{color:var(--tw);font-weight:700}
.c-item .when{color:#aaa}
.c-item .reply{color:#aaa;margin-top:3px}

/* sidebar */
.side{left:451px;width:193px}
.side-head{height:19px;background:var(--coral);color:#fff;font-family:"Roboto Condensed",sans-serif;font-weight:700;font-size:10px;line-height:19px;padding-left:8px}
.tabs{display:flex;gap:2px;margin-top:4px}
.tabs span{flex:1;height:17px;line-height:17px;text-align:center;color:#fff;font-size:9px;font-weight:700;font-family:"Roboto Condensed",sans-serif;background:var(--teal);white-space:nowrap}
.tabs span.on{background:var(--coral)}
.mini{display:flex;gap:6px;margin-top:12px;font-size:7.5px;color:#666;line-height:1.35}
.mini i{width:40px;height:48px;flex:none;background:linear-gradient(135deg,#dfeeee,#7c8c92 60%,#f2b3b6)}
.mini b{color:var(--coral);display:block;font-weight:400}
.mini.sm i{width:40px;height:40px}
.mini em{font-style:normal;color:var(--teal);display:block;margin-top:2px}
.archive{list-style:none;margin-top:8px;font-size:7.5px;color:#666}
.archive li{padding:4px 0 4px 10px;position:relative;border-bottom:1px dotted var(--line)}
.archive li::before{content:"";position:absolute;left:1px;top:7px;width:4px;height:4px;border-radius:50%;background:var(--teal)}
.cloud{margin-top:8px;font-family:"Roboto Condensed",sans-serif;line-height:1.3;color:#4e7e7a;font-size:10px}
.cloud .l{font-size:15px;color:var(--teal);font-weight:700}
.cloud .c{color:var(--coral);font-size:13px;font-weight:700}
.cloud .s{font-size:7px}
.cloud .b{color:#2b5f59;font-weight:700;font-size:12px}
.promo{margin-top:8px;height:250px;position:relative;background:linear-gradient(180deg,#ffe8a8 0%,#f3a5a8 30%,#bfe6df 55%,var(--teal) 100%)}
.promo .cap{position:absolute;left:22px;right:22px;bottom:20px;text-align:center;color:#fff;font-size:8px}
.presenter{margin-top:8px;height:250px;position:relative;background:linear-gradient(180deg,#2f97c2 0%,#8fd2e6 45%,#1d2f55 100%)}
.presenter .cap{position:absolute;left:22px;right:22px;bottom:14px;text-align:center;color:#fff;font-size:8px;background:rgba(0,0,0,.25);padding:4px}
.nav-dot{position:absolute;bottom:22px;width:14px;height:14px;border-radius:50%;background:rgba(0,0,0,.45)}
.form{margin-top:10px}
.form .f{height:26px;background:var(--teal-pale);margin-bottom:10px;font-size:8px;color:#888;line-height:26px;padding-left:22px;position:relative}
.form .f::before{content:"";position:absolute;left:8px;top:9px;width:8px;height:8px;border-radius:50%;background:#a9c9c4}
.form .msg{height:96px;background:var(--teal-pale)}
.form .submit{display:inline-block;background:var(--coral);color:#fff;font-size:9px;font-weight:700;padding:5px 9px;margin-top:10px}

/* footer */
.footer{left:0;width:690px;top:2700px;height:72px;border-top:3px solid var(--teal-pale);border-bottom:4px solid var(--teal-soft);display:flex;align-items:center;padding:0 30px;gap:12px}
.footer .brand-dot{width:44px;height:44px;flex:none}
.footer .brand-name{font-size:17px}
.footer .copy{font-family:"Roboto Condensed",sans-serif;font-size:11px;font-weight:700;white-space:nowrap}
.footer .copy span{color:var(--coral)}
.footer .connect{position:static;margin-left:auto;gap:5px}
</style>
</head>
<body>

<div class="side-ad abs" style="left:6px;top:80px" role="img" aria-label="Advertising banner with presenter photo and promo text"></div>
<div class="side-ad abs" style="left:6px;top:800px" role="img" aria-label="Advertising banner with presenter photo and promo text"></div>
<div class="side-ad abs" style="left:6px;top:1520px" role="img" aria-label="Advertising banner with presenter photo and promo text"></div>
<div class="side-ad abs" style="left:6px;top:2240px;height:540px" role="img" aria-label="Advertising banner with presenter photo and promo text"></div>
<div class="side-ad abs" style="left:954px;top:80px" role="img" aria-label="Advertising banner with presenter photo and promo text"></div>
<div class="side-ad abs" style="left:954px;top:800px" role="img" aria-label="Advertising banner with presenter photo and promo text"></div>
<div class="side-ad abs" style="left:954px;top:1520px" role="img" aria-label="Advertising banner with presenter photo and promo text"></div>
<div class="side-ad abs" style="left:954px;top:2240px;height:540px" role="img" aria-label="Advertising banner with presenter photo and promo text"></div>

<div class="page">
  <header>
    <div class="brand abs"><span class="brand-dot"></span><span class="brand-name">Nabdi TV</span></div>
    <div class="newsletter abs"><label>NEWSLETTER SUBSCRIBE</label><span class="field">Email...</span><span class="btn">SUBSCRIBE</span></div>
    <div class="connect abs"><b>GET</b> CONNECTED WITH US <i class="soc c"></i><i class="soc c"></i><i class="soc t"></i><i class="soc t"></i></div>
    <div class="header-rule abs"></div>
  </header>

  <nav class="nav abs">
    <a class="home">HOME</a><a class="dark">ABOUT US</a><a class="home">NEWS</a><a class="alt">VIDEOS</a><a class="home">BLOG</a><a>CONTACT</a>
    <span class="search">Search Here</span>
  </nav>
  <div class="hero abs" role="img" aria-label="Featured banner: channel presenter holding a gadget box in the studio"></div>

  <h2 class="sec-title abs">TOP <span>Nabdi</span> STORIES</h2>
  <span class="arrow-l abs"></span><span class="arrow-r abs"></span>
  <div class="stories abs">
    <article class="story"><div class="ph" role="img" aria-label="Festival episode photo"></div><div class="tag">MEHAR-JAN</div><p>Lorem Ipsum is simply dummy text of the printing and typesetting</p></article>
    <article class="story"><div class="ph" role="img" aria-label="Sports episode photo"></div><div class="tag">SPORTS</div><p>Lorem Ipsum is simply dummy text of the printing and typesetting</p></article>
    <article class="story"><div class="ph" role="img" aria-label="Streaming box review photo"></div><div class="tag">ORCHARD BOX</div><p>Lorem Ipsum is simply dummy text of the printing and typesetting</p></article>
  </div>

  <!-- post 1 -->
  <article class="post abs" style="top:668px">
    <div class="post-head">
      <div class="date"><div class="d">25</div><div class="m">MAR</div></div>
      <h3 class="post-title">Mobile Exhibition <span>MCX 2016</span> | Orchard in court | <span>Digital</span> | Competition Published Tech # 58</h3>
    </div>
    <p class="excerpt">Lorem Ipsum is simply dummy text of the printing and typesetting industry. Lorem Ipsum has been the industry's standard dummy text ever since the 1500s, when an unknown printer took a galley of type and scrambled it to make a type specimen book. It has survived not only five centuries, but also the leap into electronic typesetting, remaining essentially unchanged. It was popularised in the 1960s with the release of Letraset sheets containing</p>
    <div class="figure">
      <div class="main" role="img" aria-label="Episode 58 cover: presenter beside a phone, laptop and tablet"></div>
      <div class="thumbs"><i role="img" aria-label="Episode still"></i><i role="img" aria-label="Episode still"></i><i role="img" aria-label="Episode still"></i><i role="img" aria-label="Episode still"></i></div>
    </div>
    <div class="meta"><span>Category : Products</span><span class="cm">5 Comments</span><span>Read more</span></div>
    <div class="share"><span class="sb tw">Post</span><span class="cnt">1078</span><span class="sb fb">Like</span><span class="cnt">660</span><span class="sb pin">Save</span><span class="cnt">09</span><span class="icons"><i></i><i></i><i></i><i></i><i></i></span></div>
  </article>

  <!-- post 2 -->
  <article class="post abs" style="top:1226px">
    <div class="post-head">
      <div class="date"><div class="d">15</div><div class="m">MAR</div></div>
      <h3 class="post-title">Nabdi Team got <span>3rd Place</span> in iTechGulf Incu-bation Competition during <span>TECHCOM 2014</span></h3>
    </div>
    <p class="excerpt">Lorem Ipsum is simply dummy text of the printing and typesetting industry. Lorem Ipsum has been the industry's standard dummy text ever since the 1500s, when an unknown printer took a galley of type and scrambled it to make a type specimen book. It has survived not only five centuries, but also the leap into electronic typesetting, remaining essentially unchanged. It was popularised in the 1960s with the release of Letraset sheets containing</p>
    <div class="figure">
      <div class="main" style="background:linear-gradient(120deg,#e8f6f3,#bfe6df 40%,#f3a5a8 65%,#e8f6f3)" role="img" aria-label="Episode 68 cover: presenter holding a camera"></div>
      <div class="thumbs"><i role="img" aria-label="Episode still"></i><i role="img" aria-label="Episode still"></i><i role="img" aria-label="Episode still"></i><i role="img" aria-label="Episode still"></i></div>
    </div>
    <div class="meta"><span>Category : Products</span><span class="cm">5 Comments</span><span>Read more</span></div>
    <div class="share"><span class="sb tw">Post</span><span class="cnt">1078</span><span class="sb fb">Like</span><span class="cnt">660</span><span class="sb pin">Save</span><span class="cnt">09</span><span class="icons"><i></i><i></i><i></i><i></i><i></i></span></div>
  </article>

  <!-- post 3 -->
  <article class="post abs" style="top:1783px">
    <div class="post-head">
      <div class="date"><div class="d">15</div><div class="m">MAR</div></div>
      <div>
        <h3 class="post-title">Videos <span>by</span> Nabdi TV</h3>
        <p class="pub">Published on Mar 15, 2016</p>
      </div>
      <span class="pager">Previous - Next</span>
    </div>
    <p class="excerpt" style="margin-top:2px;padding-left:48px">Lorem Ipsum passages, and more recently with desktop publishing software like including versions of Lorem Ipsum.Lorem Ipsum passages, and more recently with desktop publishing software like Aldus PageMaker including versions.</p>
    <div class="video">
      <div class="screen" role="img" aria-label="Channel video player showing a city skyline at night">
        <svg class="play" width="44" height="44" viewBox="0 0 44 44"><circle cx="22" cy="22" r="21" fill="rgba(0,0,0,.55)"/><path d="M17 13 L32 22 L17 31 Z" fill="#fff"/></svg>
        <span class="bar"></span>
      </div>
      <div class="vthumbs">
        <i role="img" aria-label="Video thumbnail"></i><i role="img" aria-label="Video thumbnail"></i><i role="img" aria-label="Video thumbnail"></i><i role="img" aria-label="Video thumbnail"></i>
        <i role="img" aria-label="Video thumbnail"></i><i role="img" aria-label="Video thumbnail"></i><i role="img" aria-label="Video thumbnail"></i><i role="img" aria-label="Video thumbnail"></i>
      </div>
    </div>
    <div class="meta"><span>Category : Products</span><span class="cm">5 Comments</span><span>Read more</span></div>
    <div class="share" style="margin-top:8px"><span class="sb tw">Post</span><span class="cnt">1078</span><span class="sb fb">Like</span><span class="cnt">660</span><span class="sb pin">Save</span><span class="cnt">09</span><span class="icons"><i></i><i></i><i></i><i></i><i></i></span></div>

    <section class="comments">
      <div class="count">COMMENTS • 444</div>
      <div class="compose"><span class="av"></span><span class="box">Add a public comment...</span></div>
      <span class="sort">Top comments ▾</span>
      <div class="c-item"><span class="av"></span><div><span class="name">Nabdi</span> <span class="when">1 week ago (edited)</span><p>Great episode, thanks for the detailed review</p><p class="reply">Reply · 8</p></div></div>
      <div class="c-item"><span class="av"></span><div><span class="name">Samer Aziz</span> <span class="when">6 days ago</span><p>Looking forward to the next one</p><p class="reply">Reply · 1</p></div></div>
      <div class="c-item"><span class="av"></span><div><span class="name">Lina Haddad</span> <span class="when">1 week ago</span><p>Very useful, please cover more phones</p><p class="reply">Reply · 1</p></div></div>
      <div class="c-item"><span class="av"></span><div><span class="name">Omar Saleh</span> <span class="when">1 week ago</span><p>Well done team</p><p class="reply">Reply · 1</p></div></div>
    </section>
  </article>

  <!-- sidebar -->
  <aside class="side abs" style="top:672px">
    <div class="side-head">TOP STORIES</div>
    <div class="tabs"><span>FASHION</span><span class="on">MOBILE</span><span>ORCHARD BOX</span></div>
    <div class="mini"><i role="img" aria-label="Story photo"></i><p><b>Lorem Ipsum is simply dummy text of the printing</b>Lorem Ipsum is simply dummy text of the printing and typesetting industry. Lorem Ipsum has been the industry's</p></div>
    <div class="mini"><i role="img" aria-label="Story photo"></i><p><b>Lorem Ipsum is simply dummy text of the printing</b>Lorem Ipsum is simply dummy text of the printing and typesetting industry. Lorem Ipsum has been the industry's</p></div>
    <div class="mini"><i role="img" aria-label="Story photo"></i><p><b>Lorem Ipsum is simply dummy text of the printing</b>Lorem Ipsum is simply dummy text of the printing and typesetting industry. Lorem Ipsum has been the industry's</p></div>
  </aside>

  <aside class="side abs" style="top:956px">
    <div class="side-head">YOU MIGHT ALSO LIKE</div>
    <div class="mini sm"><i role="img" aria-label="Related post photo"></i><p>Lorem Ipsum is simply dummy text of the printing and typesetting industry.<em>Medication »</em></p></div>
    <div class="mini sm"><i role="img" aria-label="Related post photo"></i><p>Lorem Ipsum is simply dummy text of the printing and typesetting industry.<em>Medication »</em></p></div>
    <div class="mini sm"><i role="img" aria-label="Related post photo"></i><p>Lorem Ipsum is simply dummy text of the printing and typesetting industry.<em>Medication »</em></p></div>
    <div class="mini sm"><i role="img" aria-label="Related post photo"></i><p>Lorem Ipsum is simply dummy text of the printing and typesetting industry.<em>Medication »</em></p></div>
  </aside>

  <aside class="side abs" style="top:1216px">
    <div class="side-head">ARCHIVES</div>
    <ul class="archive">
      <li>Lorem Ipsum is simply dummy text of the printing and typesetting industry.</li>
      <li>Lorem Ipsum has been the industry's standard dummy text ever since the 1500s.</li>
      <li>When an unknown printer took a galley of type and scrambled it to make a type specimen book.</li>
      <li>It has survived not only five centuries, but also the leap into electronic typesetting</li>
      <li>Remaining essentially unchanged. It was popularised in the 1960s with the release of</li>
      <li>Letraset sheets containing Lorem Ipsum passages, and more recently with desktop publishing</li>
      <li>Software like Aldus PageMaker including versions of Lorem Ipsum.</li>
    </ul>
  </aside>

  <aside class="side abs" style="top:1467px">
    <div class="side-head">NABDI CLOUD</div>
    <p class="cloud"><span class="b">Nabdi</span> <span class="c">Smartphones</span> <span class="s">Wearables Chargers</span> Tablets <span class="s">Drones</span> Laptops <span class="l">Cameras</span> <span class="l">Reviews</span> <span class="b">Apps</span> <span class="s">Cloud Storage</span> Gaming <span class="b">Consoles</span> <span class="l">AI</span> <span class="s">Robotics Sensors</span> Audio <span class="l">Headphones</span> <span class="s">Smart Home</span> Routers <span class="c">Byte Notes</span> <span class="s">Batteries Cables</span> <span class="b">Security</span> <span class="b">Startups</span> <span class="l">Unboxing</span> <span class="s">Firmware</span> <span class="b">Screens</span> <span class="s">Processors</span> <span class="l">Comparisons</span> <span class="s">Tips Guides</span> Events <span class="s">Accessories</span> <span class="b">Networks</span> <span class="s">Software</span> Updates Storage <span class="b">Offers</span> Coding <span class="s">Downloads</span> Deals <span class="b">Speakers</span> <span class="c">Orchard Box</span> <span class="s">Watches</span> <span class="b">Podcasts</span> Tech</p>
  </aside>

  <aside class="side abs" style="top:1783px">
    <div class="side-head">FOLLOW US ON CLIPVANE</div>
    <div class="promo" role="img" aria-label="Channel celebration banner for reaching 100,000 subscribers">
      <span class="nav-dot" style="left:6px"></span><span class="nav-dot" style="right:6px"></span>
      <p class="cap">Lorem ipsum dolor sit amet consectetur adipiscing elit, sed justo pulvinar.</p>
    </div>
  </aside>

  <aside class="side abs" style="top:2089px">
    <div class="side-head">OUR NEWS PRESENTER</div>
    <div class="presenter" role="img" aria-label="Portrait of the channel news presenter">
      <span class="nav-dot" style="left:6px"></span><span class="nav-dot" style="right:6px"></span>
      <p class="cap">Lorem ipsum dolor sit amet consectetur adipiscing elit sed justo pulvinar.</p>
    </div>
  </aside>

  <aside class="side abs" style="top:2382px">
    <div class="side-head">CONTACT US</div>
    <form class="form">
      <div class="f">Enter your name</div>
      <div class="f">Enter your email address</div>
      <div class="f">Enter your website url</div>
      <div class="msg"></div>
      <span class="submit">Submit Interest</span>
    </form>
  </aside>

  <footer class="footer abs">
    <span class="brand-dot"></span><span class="brand-name">Nabdi TV</span>
    <p class="copy"><span>COPYRIGHT</span> © 2016 <span>NABDITV</span>. All Rights Reserved</p>
    <div class="connect">Get <b>Connected</b> With Us <i class="soc c"></i><i class="soc c"></i><i class="soc t"></i><i class="soc t"></i></div>
  </footer>
</div>

</body>
</html>
```